Founder / concept developer needs business card // Consultant needs VCARD

I need a business card for me as a founding consultant in Berlin. I advise entrepreneurs, especially in the design of business ideas, business plans or financing applications. More information about this in the annexes. My USP: I design / structure complex ideas and projects convincingly so that my client is successful. I want to communicate professionalism, effectiveness and clarity. Colors like from the range BLACK-GRAY-GREEN. I am 27 years old, I have studied business for 7 years. Attachments: - Business card design (only idea, do not focus on it) - Website screenshot (only idea, do not focus on it)

Target Market(s)

Target group: Founder (20-50 yrs, m / w, needy, in "break-up phase") and CONTRACTOR / "financier" (30-55 yrs, m / w, often public service "routine-oriented"). The foundations are in quite different industries: digital, craft, tourism, retail, services, etc. Almost all German.

Industry/Entity Type

Consultant

Contact Information for Business Card

Lukas Brandvik
M. Sc., International Business Administration
Gründungsberater, Konzeptentwickler
www.falkenhorn-beratung.de
kontakt@falkenhorn-beratung.de
Tel. 0471 239 5518

Colors

Designer to choose colors to be used in the design.

Requirements
Must have
• Professionalism, persuasiveness, clarity
Nice to have
• memorability
Should not have
• Schnörkelei

```html
<!DOCTYPE html>
<html lang="de">
<head>
<meta charset="utf-8">
<title>Visitenkarte – Lukas Brandvik</title>
<link rel="stylesheet" href="https://fonts.googleapis.com/css2?family=Arimo:wght@400;700&display=swap">
<style>
  :root {
    --bg: #efefef;
    --slate: #363a45;
    --paper: #ffffff;
    --ink: #2f333d;
    --ink-soft: #5d6169;
    --ink-muted: #7a7d84;
  }
  * { box-sizing: border-box; margin: 0; padding: 0; }
  html, body {
    width: 1200px;
    height: 1054px;
    overflow: hidden;
    background: var(--bg);
    font-family: "Arimo", Arial, sans-serif;
  }
  .canvas {
    position: relative;
    width: 1200px;
    height: 1054px;
  }
  .card {
    position: absolute;
    width: 560px;
    height: 362px;
    box-shadow: 0 2px 6px rgba(0,0,0,0.12);
  }
  .card--back {
    left: 70px;
    top: 120px;
    background: var(--slate);
    display: flex;
    align-items: center;
    justify-content: center;
    gap: 16px;
  }
  .card--back .mark-square {
    width: 58px;
    height: 58px;
    background: var(--paper);
  }
  .card--back .mark-name {
    color: var(--paper);
    font-weight: 700;
    font-size: 22px;
    letter-spacing: 0.04em;
    text-transform: uppercase;
  }
  .card--front {
    left: 570px;
    top: 570px;
    background: var(--paper);
    display: flex;
    flex-direction: column;
    align-items: center;
    text-align: center;
    padding-top: 58px;
  }
  .card--front .mark-square {
    width: 62px;
    height: 62px;
    background: var(--slate);
    margin-bottom: 22px;
  }
  .holder-name {
    color: var(--ink);
    font-weight: 700;
    font-size: 25px;
    letter-spacing: 0.02em;
    text-transform: uppercase;
    margin-bottom: 8px;
  }
  .holder-role {
    color: var(--ink-soft);
    font-size: 14.5px;
    line-height: 1.3;
  }
  .contact-line {
    margin-top: auto;
    margin-bottom: 48px;
    color: var(--ink-muted);
    font-size: 13.5px;
    letter-spacing: 0.01em;
  }
  .contact-line .sep { margin: 0 6px; }
</style>
</head>
<body>
<main class="canvas">
  <section class="card card--back" aria-label="Kartenrückseite">
    <span class="mark-square"></span>
    <span class="mark-name">Lukas Brandvik</span>
  </section>

  <section class="card card--front" aria-label="Kartenvorderseite">
    <span class="mark-square"></span>
    <h1 class="holder-name">Lukas Brandvik</h1>
    <p class="holder-role">M. Sc., International Business Administration</p>
    <p class="holder-role">Gründungsberater, Konzeptentwickler</p>
    <p class="contact-line">
      0471 239 5518<span class="sep">/</span>kontakt@falkenhorn-beratung.de<span class="sep">/</span>www.falkenhorn-beratung.de
    </p>
  </section>
</main>
</body>
</html>
```